Recreate a label for a champagne bottle [See attached example]

I'm needing to recreate a label for a champagne bottle label to give as closing gifts to clients when they purchase a home. Please include the following text "Welcome Home", my initials "R.T", "Established Year", the hashtag #BubbLORNE and my logo (attached). I prefer to have a black or white background with a crisp, easy to read cursive font similar to the Dunmore bourbon font. I want it to look as similar of a layout to the Valcorta label as possible

Target Market(s)

Luxury

Font styles to use
Decorative
Script

Colors

Designer to choose only greyscale colors for use in the design.

Requirements
Must have
• "Welcome Home", my initials "R.T", "Established Year", the hashtag #BubbLORNE and my logo
Nice to have
• Clean cursive font, easy to read, luxury look.
Should not have
• Clutter, too much design.

```html
<!DOCTYPE html>
<html lang="en">
<head>
<meta charset="utf-8">
<title>Welcome Home – Champagne Label</title>
<link rel="stylesheet" href="https://fonts.googleapis.com/css2?family=Pinyon+Script&family=Cormorant+Garamond:wght@500&family=Open+Sans:wght@600&display=swap">
<style>
  :root {
    --page: #ffffff;
    --label-edge: #000000;
    --label-mid: #262626;
    --badge: #1c1c1c;
    --gold: #c9a85a;
    --gold-light: #e6d3a3;
    --gold-soft: rgba(201, 168, 90, 0.18);
  }
  * { margin: 0; padding: 0; box-sizing: border-box; }
  html, body {
    width: 1200px;
    height: 1000px;
    overflow: hidden;
    background: var(--page);
  }
  .label {
    position: relative;
    width: 1200px;
    height: 1000px;
  }
  .label-shape {
    position: absolute;
    inset: 0;
  }
  .brand-name {
    position: absolute;
    left: 480px;
    top: 212px;
    width: 240px;
    text-align: center;
    font-family: "Cormorant Garamond", serif;
    font-weight: 500;
    font-size: 30px;
    letter-spacing: 1px;
    color: var(--gold);
  }
  .headline {
    position: absolute;
    left: 0;
    top: 440px;
    width: 1200px;
    text-align: center;
    font-family: "Pinyon Script", cursive;
    font-size: 66px;
    line-height: 1;
    color: var(--gold-light);
    text-shadow: 0 2px 3px rgba(0, 0, 0, 0.8);
  }
  .initials {
    position: absolute;
    left: 0;
    top: 538px;
    width: 1200px;
    text-align: center;
    font-family: "Cormorant Garamond", serif;
    font-weight: 500;
    font-size: 27px;
    color: var(--gold);
  }
  .established {
    position: absolute;
    left: 470px;
    top: 624px;
    width: 260px;
    text-align: center;
    font-family: "Cormorant Garamond", serif;
    font-weight: 500;
    font-size: 24px;
    letter-spacing: 0.5px;
    color: var(--gold);
  }
  .hashtag {
    position: absolute;
    left: 0;
    top: 738px;
    width: 1200px;
    text-align: center;
    font-family: "Open Sans", sans-serif;
    font-weight: 600;
    font-size: 16px;
    letter-spacing: 1.5px;
    color: var(--gold-light);
  }
</style>
</head>
<body>
<div class="label">
  <svg class="label-shape" width="1200" height="1000" viewBox="0 0 1200 1000" aria-hidden="false">
    <defs>
      <linearGradient id="labelFill" x1="0" y1="0" x2="1" y2="0">
        <stop offset="0" stop-color="var(--label-edge)"/>
        <stop offset="0.5" stop-color="var(--label-mid)"/>
        <stop offset="1" stop-color="var(--label-edge)"/>
      </linearGradient>
      <radialGradient id="wreathFill" cx="0.5" cy="0.5" r="0.5">
        <stop offset="0.72" stop-color="var(--badge)"/>
        <stop offset="0.86" stop-color="var(--gold-soft)"/>
        <stop offset="1" stop-color="var(--badge)"/>
      </radialGradient>
    </defs>

    <path class="label-body" fill="url(#labelFill)"
      d="M300,250 Q450,244 600,236 Q750,244 900,250 C915,255 910,290 912,300 C915,322 963,320 963,362
         L963,790 C963,830 915,826 910,850 C905,880 920,895 880,898 Q740,906 600,938
         Q460,906 320,898 C280,895 295,880 290,850 C285,826 237,830 237,790
         L237,362 C237,320 285,322 288,300 C290,290 285,255 300,250 Z"/>

    <path class="inner-frame" fill="none" stroke="var(--gold)" stroke-width="2"
      d="M380,330 L820,330 C842,330 832,380 852,385 C870,390 872,400 872,422
         L872,720 C872,745 866,752 850,756 C830,762 842,810 800,815 Q700,825 600,848
         Q500,825 400,815 C358,810 370,762 350,756 C334,752 328,745 328,720
         L328,422 C328,400 330,390 348,385 C368,380 358,330 380,330 Z"/>

    <circle class="badge" cx="600" cy="230" r="155" fill="var(--badge)" stroke="var(--gold)" stroke-width="3"/>
    <circle class="badge-wreath" cx="600" cy="230" r="140" fill="url(#wreathFill)"
      role="img" aria-label="Gold leaf wreath ornament circling the logo"/>

    <g class="established-band" stroke="var(--gold)" stroke-width="1.5">
      <line x1="470" y1="622" x2="730" y2="622"/>
      <line x1="470" y1="661" x2="730" y2="661"/>
    </g>
    <rect class="flourish flourish-left" x="444" y="622" width="26" height="40" rx="6" fill="var(--gold-soft)"
      role="img" aria-label="Small gold scroll flourish"/>
    <rect class="flourish flourish-right" x="730" y="622" width="26" height="40" rx="6" fill="var(--gold-soft)"
      role="img" aria-label="Small gold scroll flourish"/>
  </svg>

  <div class="brand-name">Tarrow Homes</div>
  <div class="headline">"Welcome home"</div>
  <div class="initials">– R.T –</div>
  <div class="established">ESTABLISHED : 2023</div>
  <div class="hashtag">#BubbLORNE</div>
</div>
</body>
</html>
```